Design for album cover

Looking for a creative design for an album cover for an unreleased song I wrote called "DRIFT". It's about regrets over a failed toxic relationship.
You can preview the song at the following link...
http://www.tunelofter.com/control_room/artist/5817402/songs

Reason: to allow designers to come up with better designs

```html
<!DOCTYPE html>
<html lang="en">
<head>
<meta charset="utf-8">
<title>LeoMarsh – Drift</title>
<link href="https://fonts.googleapis.com/css2?family=Cinzel:wght@400;500&display=swap" rel="stylesheet">
<style>
  :root {
    --sky-top: #f6f3f1;
    --sky-mid: #e7e1de;
    --sky-low: #cfc8c5;
    --horizon: #d9d3d0;
    --sea-far: #b7b1ad;
    --sea-near: #8d8683;
    --surf: #5f5957;
    --sand-wet: #a49b95;
    --sand: #b8afa9;
    --sand-low: #a9a09a;
    --ink: #2f2b2a;
  }
  html, body {
    margin: 0;
    padding: 0;
    width: 1200px;
    height: 1200px;
    overflow: hidden;
  }
  .album-cover {
    position: relative;
    width: 1200px;
    height: 1200px;
    overflow: hidden;
  }
  .cover-photo {
    position: absolute;
    inset: 0;
    background: linear-gradient(
      to bottom,
      var(--sky-top) 0%,
      var(--sky-mid) 22%,
      var(--sky-low) 38%,
      var(--horizon) 46.8%,
      var(--sea-far) 47%,
      var(--sea-far) 51%,
      var(--sea-near) 54%,
      var(--surf) 55.5%,
      var(--sand-wet) 57%,
      var(--sand) 62%,
      var(--sand) 80%,
      var(--sand-low) 100%
    );
  }
  .cover-title {
    position: absolute;
    left: 0;
    right: 0;
    top: 938px;
    text-align: center;
    color: var(--ink);
    font-family: "Cinzel", "Trajan Pro", serif;
    margin: 0;
  }
  .artist-name {
    display: block;
    font-size: 128px;
    font-weight: 400;
    line-height: 1;
    letter-spacing: 0.01em;
  }
  .song-title {
    display: block;
    margin-top: 6px;
    font-size: 64px;
    font-weight: 400;
    line-height: 1;
    letter-spacing: 0.42em;
    padding-left: 0.42em;
  }
</style>
</head>
<body>
  <main class="album-cover">
    <div class="cover-photo" role="img" aria-label="Muted, desaturated photo of a lone man walking across a wide windswept beach toward the sea under an overcast sky"></div>
    <h1 class="cover-title">
      <span class="artist-name">LeoMarsh</span>
      <span class="song-title">DRIFT</span>
    </h1>
  </main>
</body>
</html>
```